ZiPU Vortal Bhutan Trip

This is a one-page (A5) flyer to attract sign ups for Bhutan Trip.

Target Market(s)

Young entrepreneurs (worldwide)

Requirements
Must have
• Must have "WOW" effect and attract sign ups
Nice to have
• Striking and vibrant

```html
<!DOCTYPE html>
<html lang="en">
<head>
<meta charset="utf-8">
<title>ZiPU Vortal Bhutan Trip</title>
<link href="https://fonts.googleapis.com/css2?family=Bangers&family=Permanent+Marker&family=Roboto+Condensed:ital,wght@0,400;0,700;1,700&family=Roboto:wght@400;700;900&display=swap" rel="stylesheet">
<style>
  :root {
    --page-bg: #e9e9e9;
    --paper: #ffffff;
    --orange: #f39237;
    --red: #e31e26;
    --black: #111111;
    --lime: #b5d334;
    --tick: #9ccc2e;
    --ink: #1b1b1b;
    --grey: #555555;
    --cream: #fff3c9;
    --blue: #2f4f9e;
    --brand-orange: #f5822a;
    --brand-green: #8cc63f;
    --brand-blue: #1fa4dc;
    --brand-pink: #ec4c9c;
    --brand-purple: #c2188f;
    --partner-green: #3d8b3d;
    --partner-teal: #1f6e8c;
    --partner-navy: #1d3f7a;
  }
  * { box-sizing: border-box; margin: 0; padding: 0; }
  html, body { width: 1200px; height: 1200px; overflow: hidden; background: var(--page-bg); }
  body { position: relative; font-family: "Roboto Condensed", sans-serif; }

  .flyer {
    position: absolute; left: 194px; top: 24px;
    width: 854px; height: 1212px;
    transform: scale(0.95); transform-origin: top left;
    background: var(--paper); overflow: hidden;
  }
  .flyer > * { position: absolute; }

  .presenter-note {
    left: 165px; top: 70px; width: 140px;
    font-family: "Roboto", sans-serif; font-size: 19px; line-height: 25px;
    color: var(--grey); text-align: right; transform: rotate(-20deg);
  }
  .client-name {
    left: 330px; top: 95px; width: 270px; text-align: center;
    font-family: "Roboto", sans-serif; font-weight: 900; font-size: 54px;
    color: var(--ink); letter-spacing: 1px;
  }

  .hero-photo {
    left: 0; top: 150px; width: 854px; height: 470px;
    background:
      linear-gradient(180deg, #ffffff 0%, rgba(255,255,255,0) 22%),
      radial-gradient(ellipse 30% 42% at 50% 55%, #b4312a 0%, #8e3a2c 45%, rgba(142,58,44,0) 100%),
      linear-gradient(180deg, #d5dde6 20%, #9cb1c4 45%, #5f6a58 62%, #8d8a83 80%, #6e6760 100%);
    clip-path: polygon(0 0, 100% 0, 100% 96%, 0 96%);
  }

  .trip-title {
    left: 95px; top: 462px; width: 700px;
    font-family: "Bangers", sans-serif; font-size: 118px; line-height: 1;
    letter-spacing: 2px; white-space: nowrap;
    -webkit-text-stroke: 3px #ffffff; paint-order: stroke fill;
    text-shadow: 4px 5px 0 rgba(0,0,0,.35);
  }
  .trip-title .l1 { color: var(--brand-orange); }
  .trip-title .l2 { color: var(--red); }
  .trip-title .l3 { color: var(--brand-green); }
  .trip-title .l4 { color: var(--brand-blue); }
  .trip-title .l5 { color: var(--brand-pink); }
  .trip-title .l6 { color: var(--brand-purple); }
  .trip-title .dark { color: var(--black); }

  .orange-band {
    left: 0; top: 598px; width: 854px; height: 192px; background: var(--orange);
  }
  .date-pill {
    left: 180px; top: 588px; width: 498px; height: 62px; border-radius: 22px;
    background: var(--black); color: #fff; text-align: center;
    font-family: "Permanent Marker", cursive; font-size: 42px; line-height: 62px; letter-spacing: 1px;
  }
  .sign-up {
    left: 34px; top: 660px;
    font-family: "Roboto Condensed", sans-serif; font-style: italic; font-weight: 700;
    font-size: 96px; line-height: 1; color: var(--cream);
    -webkit-text-stroke: 3px var(--red); paint-order: stroke fill;
    text-shadow: 3px 4px 0 rgba(120,30,0,.35);
  }
  .sign-up-underline { left: 40px; top: 752px; width: 390px; height: 22px; }
  .brace { left: 432px; top: 660px; width: 40px; height: 118px; }
  .tagline {
    left: 486px; top: 664px; width: 340px;
    font-size: 31px; line-height: 37px; color: #fff;
  }

  .red-band {
    left: 0; top: 789px; width: 854px; height: 264px; background: var(--red);
  }
  .highlights-label {
    left: 44px; top: 1032px; transform: rotate(-90deg); transform-origin: top left;
    font-family: "Roboto", sans-serif; font-weight: 700; font-size: 22px;
    letter-spacing: 8px; color: #fff; white-space: nowrap; width: 230px;
  }
  .highlights {
    left: 84px; top: 804px; list-style: none;
  }
  .highlights li {
    display: flex; align-items: center; height: 40.8px;
    font-size: 24px; color: #fff; white-space: nowrap;
  }
  .highlights li svg { width: 30px; height: 28px; margin-right: 16px; flex: none; }
  .highlights b { font-weight: 700; margin-right: 6px; }

  .price-badge { left: 558px; top: 812px; width: 290px; height: 270px; }
  .price-text {
    left: 568px; top: 848px; width: 264px; text-align: center;
    font-family: "Roboto", sans-serif; color: var(--ink);
  }
  .price-text .small { font-size: 22px; line-height: 24px; }
  .price-text .big { font-size: 40px; font-weight: 900; line-height: 40px; }
  .price-text .huge { font-size: 50px; font-weight: 900; line-height: 50px; }
  .price-text .note { font-size: 13.5px; line-height: 16px; }
  .price-text .rule { height: 1px; background: rgba(0,0,0,.25); margin: 6px 28px 6px; }

  .supported-by {
    left: 54px; top: 1070px; font-family: "Roboto", sans-serif; font-size: 15px; color: var(--ink);
  }
  .partner {
    top: 1122px; display: flex; align-items: center; gap: 8px;
    font-family: "Roboto", sans-serif; font-weight: 700; font-size: 22px; white-space: nowrap;
  }
  .partner .dot { width: 26px; height: 26px; border-radius: 50%; }
  .partner-a { left: 62px; color: var(--partner-green); }
  .partner-a .dot { background: var(--partner-green); }
  .partner-b { left: 205px; color: var(--partner-teal); }
  .partner-c { left: 385px; color: var(--partner-navy); }
  .partner-c .dot { background: var(--partner-navy); border-radius: 0; }
  .footer-divider { left: 512px; top: 1072px; width: 2px; height: 112px; background: var(--grey); }
  .register {
    left: 530px; top: 1082px; width: 310px; text-align: center; font-family: "Roboto", sans-serif;
  }
  .register h2 { font-size: 34px; font-weight: 900; font-style: italic; color: var(--ink); line-height: 40px; }
  .register .limit { font-size: 23px; color: var(--red); line-height: 32px; margin-top: 2px; }
  .register .email { font-size: 23px; color: var(--blue); line-height: 32px; }
</style>
</head>
<body>
<div class="flyer">
  <div class="presenter-note">Exclusively<br>Brought<br>To You By:</div>
  <div class="client-name">ZiPU Vortal</div>

  <div class="hero-photo" role="img" aria-label="Photo of a traditional Bhutanese temple with red and white walls in a stone courtyard, mountains and cloudy sky behind"></div>

  <div class="orange-band"></div>

  <h1 class="trip-title"><span class="l1">B</span><span class="l2">H</span><span class="l3">U</span><span class="l4">T</span><span class="l5">A</span><span class="l6">N</span> <span class="dark">TRIP</span></h1>

  <div class="date-pill">3-6 JULY 2017</div>

  <div class="sign-up">SIGN UP</div>
  <svg class="sign-up-underline" viewBox="0 0 390 22"><path d="M4 18 Q200 4 386 6 L386 12 Q200 12 4 18 Z" fill="#fff"/></svg>
  <svg class="brace" viewBox="0 0 40 118"><path d="M4 2 Q22 4 22 24 L22 46 Q22 58 36 59 Q22 60 22 72 L22 94 Q22 114 4 116" fill="none" stroke="#fff" stroke-width="3"/></svg>
  <p class="tagline">for a once in a lifetime experience in the land of happiness!</p>

  <div class="red-band"></div>
  <div class="highlights-label">HIGHLIGHTS</div>
  <ul class="highlights">
    <li><svg viewBox="0 0 30 28"><path d="M3 15 L11 24 L27 3" fill="none" stroke="#9ccc2e" stroke-width="6" stroke-linecap="round" stroke-linejoin="round"/></svg><b>LEARN</b> from Leading Social Change Makers</li>
    <li><svg viewBox="0 0 30 28"><path d="M3 15 L11 24 L27 3" fill="none" stroke="#9ccc2e" stroke-width="6" stroke-linecap="round" stroke-linejoin="round"/></svg><b>ENGAGE</b> the community through volunteering</li>
    <li><svg viewBox="0 0 30 28"><path d="M3 15 L11 24 L27 3" fill="none" stroke="#9ccc2e" stroke-width="6" stroke-linecap="round" stroke-linejoin="round"/></svg><b>DISCOVER</b> your inner happiness</li>
    <li><svg viewBox="0 0 30 28"><path d="M3 15 L11 24 L27 3" fill="none" stroke="#9ccc2e" stroke-width="6" stroke-linecap="round" stroke-linejoin="round"/></svg><b>SAVOUR</b> organic food</li>
    <li><svg viewBox="0 0 30 28"><path d="M3 15 L11 24 L27 3" fill="none" stroke="#9ccc2e" stroke-width="6" stroke-linecap="round" stroke-linejoin="round"/></svg><b>IMMERSE</b> in traditional sports and craft</li>
    <li><svg viewBox="0 0 30 28"><path d="M3 15 L11 24 L27 3" fill="none" stroke="#9ccc2e" stroke-width="6" stroke-linecap="round" stroke-linejoin="round"/></svg><b>EXPERIENCE</b> warm Bhutanese hospitality</li>
  </ul>

  <svg class="price-badge" viewBox="0 0 290 270">
    <path d="M145 4 C220 4 280 60 280 132 C280 175 262 205 240 222 C210 218 150 226 84 262 C74 240 62 228 46 215 C20 192 4 160 4 132 C4 60 68 4 145 4 Z" fill="#b5d334"/>
  </svg>
  <div class="price-text">
    <div class="small">PRICE AT</div>
    <div class="big">USD 2800</div>
    <div class="rule"></div>
    <div class="small">EARLY BIRD DISCOUNT</div>
    <div class="huge">USD 2300</div>
    <div class="note">(If you sign up by 31 March 2017)</div>
  </div>

  <div class="supported-by">SUPPORTED BY</div>
  <div class="partner partner-a"><span class="dot"></span>Tera Circle</div>
  <div class="partner partner-b">Travoxa</div>
  <div class="partner partner-c"><span class="dot"></span>Kindora</div>
  <div class="footer-divider"></div>
  <div class="register">
    <h2>REGISTER NOW!</h2>
    <p class="limit">Limited to 30 participants!</p>
    <p class="email">Email: hello@teracircle.org</p>
  </div>
</div>
</body>
</html>
```